Simple, Professional and neat business card design for Vendralo Inc.

We're looking to re-vamp our business card design. We're a supplier of innovative feed ingredients for the North American animal agriculture industry. We are located in Lucknow, Ontario, Canada and our flagship product is a product that prevents milk fever in dairy cows when the calve, it is fed before calving and is very effective compared to other alternatives available on the market today.

Our company has Danish roots and we import all of our product from our Danish partner/manufacturer in Denmark. We like our design to embrace high professionalism while remaining neat and simple.

Target Market(s)

B2B, Feed Mills, Veterinary Clinics, Large integrators/producers,

Industry/Entity Type

Agribusiness

Contact Information for Business Card

We like the rounded corners because they make the card easy to sit in a wallet and not many use it so it makes the card stand out, just possibly something to take account for during the design.

As you can also see on the sliders below, looking for a that simple but proffesional scandinavian design.

Requirements
Nice to have
• Rounded corners
Should not have
• Too vibrant

```html
<!DOCTYPE html>
<html lang="en">
<head>
<meta charset="utf-8">
<title>Vendralo Inc. – Business Card</title>
<link rel="stylesheet" href="https://fonts.googleapis.com/css2?family=Open+Sans:wght@400;600;700&display=swap">
<style>
  :root {
    --backdrop: #3b332e;
    --card: #141414;
    --card-edge: #1d1d1d;
    --brand-blue: #1f5fae;
    --text-grey: #c9c9c9;
    --rule: #5a5a5a;
    --tagline: #e6e6e6;
    --dot: #6d6d6d;
  }
  * { box-sizing: border-box; margin: 0; padding: 0; }
  html, body { width: 1200px; height: 844px; overflow: hidden; }
  body {
    background: var(--backdrop);
    font-family: "Open Sans", Arial, sans-serif;
    position: relative;
  }
  .card {
    position: absolute;
    width: 520px;
    height: 300px;
    background: var(--card);
    border: 1px solid var(--card-edge);
    border-radius: 18px;
    top: 272px;
    box-shadow: 0 14px 30px rgba(0,0,0,.45);
  }
  .card--contact { left: 45px; }
  .card--brand { left: 635px; }

  /* contact side */
  .brand-block {
    position: absolute;
    left: 34px; top: 0; bottom: 0;
    width: 230px;
    display: flex; flex-direction: column; justify-content: center; align-items: center;
    gap: 18px;
  }
  .brand-mark {
    width: 58px; height: 58px; border-radius: 50%;
    background: var(--brand-blue);
  }
  .brand-name {
    color: var(--brand-blue);
    font-weight: 700; font-size: 30px; letter-spacing: .5px;
    white-space: nowrap;
  }
  .divider {
    position: absolute; left: 278px; top: 60px; bottom: 60px;
    width: 1px; background: var(--rule);
  }
  .details {
    position: absolute; left: 300px; top: 52px;
    color: var(--text-grey);
  }
  .person-name {
    color: var(--brand-blue); font-weight: 600; font-size: 16px;
    letter-spacing: .6px; margin-bottom: 10px;
  }
  .contact-list { list-style: none; font-size: 14px; line-height: 20px; }
  .contact-list li { display: flex; align-items: center; gap: 8px; }
  .contact-list svg { width: 11px; height: 11px; flex: none; fill: var(--brand-blue); }
  .address { font-size: 14px; line-height: 19px; margin-top: 6px; }

  /* brand side */
  .brand-side {
    position: absolute; inset: 0;
    display: flex; flex-direction: column; align-items: center;
    padding-top: 58px;
  }
  .brand-side .brand-mark { width: 64px; height: 64px; }
  .brand-side .brand-name { font-size: 24px; margin-top: 12px; }
  .tagline-rule { width: 300px; height: 1px; background: var(--rule); margin-top: 18px; }
  .tagline {
    color: var(--tagline); font-size: 11px; font-weight: 600;
    letter-spacing: 1px; margin-top: 12px;
  }
  .social-row { display: flex; gap: 6px; margin-top: 12px; margin-bottom: 14px; }
  .social-dot { width: 20px; height: 20px; border-radius: 50%; background: var(--dot); }
</style>
</head>
<body>

<section class="card card--contact" aria-label="Business card, contact side">
  <div class="brand-block">
    <div class="brand-mark"></div>
    <div class="brand-name">VENDRALO INC.</div>
  </div>
  <div class="divider"></div>
  <div class="details">
    <p class="person-name">MADS HALVORSEN</p>
    <ul class="contact-list">
      <li><svg viewBox="0 0 10 10"><rect x="2.5" y="0" width="5" height="10" rx="1"/></svg>555-214-0387</li>
      <li><svg viewBox="0 0 10 10"><rect x="2.5" y="0" width="5" height="10" rx="1"/></svg>555-306-4419</li>
      <li><svg viewBox="0 0 10 10"><path d="M1 3 Q5 0 9 3 L8 5 L6 4 L6 3 L4 3 L4 4 L2 5 Z M2 6 H8 V10 H2 Z"/></svg>888-555-0162</li>
      <li><svg viewBox="0 0 10 10"><rect x="2" y="0" width="6" height="3"/><rect x="0" y="3" width="10" height="5" rx="1"/><rect x="2" y="7" width="6" height="3"/></svg>555-306-4420</li>
      <li><svg viewBox="0 0 10 10"><path d="M0 2 H10 V8 H0 Z M0 2 L5 6 L10 2" stroke="#141414" stroke-width=".8"/></svg>mads@vendralo.com</li>
      <li><svg viewBox="0 0 10 10"><circle cx="5" cy="5" r="5"/></svg>www.vendralo.com</li>
    </ul>
    <p class="address">Box 482, Maplebrook<br>Ontario Canada K0L 3B0</p>
  </div>
</section>

<section class="card card--brand" aria-label="Business card, brand side">
  <div class="brand-side">
    <div class="brand-mark"></div>
    <div class="brand-name">VENDRALO INC.</div>
    <div class="tagline-rule"></div>
    <p class="tagline">PROTECTING THE HEALTH OF YOUR ANIMALS</p>
    <div class="social-row">
      <span class="social-dot"></span>
      <span class="social-dot"></span>
      <span class="social-dot"></span>
      <span class="social-dot"></span>
      <span class="social-dot"></span>
    </div>
    <div class="tagline-rule" style="margin-top:0"></div>
  </div>
</section>

</body>
</html>
```